Business Card Design

Copper Reef Coach Lines, name was derived from the Copper Reef jack (fish). We are a school bus charter service that offers supplemental bus transportation to district schools for field trips, school sporting events, etc. We also offer bus service to recreation centers during summer time for field trips.
Our business incorporates the color sea or royal blue, school bus yellow and a dark or charcoal gray. Its a copy of the fish's natural color scheme.

I am looking for a logo with the color scheme listed. I am looking for something modern and professional.

Target Market(s)

School Administrators, City employees

Industry/Entity Type

Recreation

Contact Information for Business Card

Copper Reef Coach Lines LLC
Safe Reliable Affordable
Dennis Harplomack, Owner
P.O.BOX 28617
St. Petersburg, Fl 33719
727-555-0193
www.ridecopperreef.example
ridecopperreef@mailbox.example

Requirements
Should not have
• pictures of fish or buses

```html
<!DOCTYPE html>
<html lang="en">
<head>
<meta charset="utf-8">
<title>Copper Reef Coach Lines – Business Card</title>
<link href="https://fonts.googleapis.com/css2?family=Jost:wght@400;500;700&display=swap" rel="stylesheet">
<style>
  :root {
    --navy: #0f2a4f;
    --yellow: #f2bb16;
    --charcoal: #6f6b6b;
    --ink: #1d1d1f;
    --card: #f1f0ee;
    --backdrop: #8d8e91;
  }
  * { box-sizing: border-box; margin: 0; padding: 0; }
  html, body { width: 1200px; height: 1200px; overflow: hidden; }
  body {
    background: var(--backdrop);
    display: flex; align-items: center; justify-content: center;
    font-family: "Jost", sans-serif;
  }
  .business-card {
    position: relative;
    width: 1000px; height: 572px;
    background: var(--card);
    box-shadow: 0 18px 40px rgba(0,0,0,.25);
    overflow: hidden;
  }
  .brand-square {
    position: absolute; left: 44px; top: 34px;
    width: 112px; height: 112px;
    background: var(--navy);
    border-radius: 10px;
  }
  .company-name {
    position: absolute; left: 196px; top: 58px;
    font-size: 44px; font-weight: 500; letter-spacing: 2px;
    color: var(--navy); text-transform: uppercase; white-space: nowrap;
  }
  .company-name small { font-size: 22px; }
  .tagline {
    position: absolute; left: 198px; top: 120px;
    font-size: 24px; letter-spacing: 7px; color: var(--ink);
  }
  .name-band {
    position: absolute; left: 0; right: 40px; top: 172px; height: 62px;
    background: var(--yellow);
    display: flex; align-items: baseline;
    padding: 4px 0 0 260px;
    white-space: nowrap;
  }
  .owner-name {
    font-size: 40px; font-weight: 700; color: var(--navy);
    line-height: 52px;
  }
  .owner-title {
    margin-left: 14px;
    font-size: 24px; color: var(--charcoal);
    position: relative; top: 6px;
  }
  .contact-list {
    position: absolute; left: 48px; top: 280px;
    list-style: none; font-size: 27px; color: var(--ink);
  }
  .contact-list li { display: flex; align-items: center; gap: 14px; height: 42px; }
  .contact-list svg { width: 22px; height: 22px; }
  .mailing-address {
    position: absolute; right: 70px; top: 352px;
    font-size: 30px; font-weight: 500; color: var(--ink);
    text-align: right; line-height: 42px; font-style: normal;
  }
  .mailing-address svg {
    position: absolute; left: -40px; top: 4px; width: 30px; height: 34px;
  }
</style>
</head>
<body>
  <div class="business-card">
    <div class="brand-square"></div>
    <div class="company-name">Copper Reef Coach Lines <small>LLC</small></div>
    <div class="tagline">Safe ~ Reliable ~ Affordable</div>

    <div class="name-band">
      <span class="owner-name">Dennis Harplomack,</span>
      <span class="owner-title">Owner</span>
    </div>

    <ul class="contact-list">
      <li>
        <svg viewBox="0 0 24 24" fill="none" stroke="#0f2a4f" stroke-width="2"><path d="M5 3h4l2 5-3 2a12 12 0 0 0 6 6l2-3 5 2v4a2 2 0 0 1-2 2A17 17 0 0 1 3 5a2 2 0 0 1 2-2z"/></svg>
        727-555-0193
      </li>
      <li>
        <svg viewBox="0 0 24 24" fill="none" stroke="#0f2a4f" stroke-width="2"><circle cx="12" cy="12" r="4"/><path d="M16 12v1.5a2.5 2.5 0 0 0 5 0V12a9 9 0 1 0-4 7.5"/></svg>
        www.ridecopperreef.example
      </li>
      <li>
        <svg viewBox="0 0 24 24" fill="none" stroke="#0f2a4f" stroke-width="2"><rect x="3" y="5" width="18" height="14" rx="1"/><path d="M3 6l9 7 9-7"/></svg>
        ridecopperreef@mailbox.example
      </li>
    </ul>

    <address class="mailing-address">
      <svg viewBox="0 0 24 28" fill="none" stroke="#0f2a4f" stroke-width="2.2"><path d="M12 26s9-9 9-15a9 9 0 0 0-18 0c0 6 9 15 9 15z"/><circle cx="12" cy="11" r="3.5"/></svg>
      P.O.BOX 28617<br>
      St. Petersburg<br>
      Fl 33719
    </address>
  </div>
</body>
</html>
```